Create a business promotion flyer to leave in customer mailboxes. We are a bulk petroleum supplier, servicing any industry that requires diesel. Base in griffith NSW, servicing griffith area and surrounds.

Business Name - Terra Petro
Fuel@terrapetro-example.com.au
Marco - 0400 000 001 mtorrisi@terrapetro-example.com.au
Liam - 0400 000 002 lharcourt@terrapetro-example.com.au
Peter - 0400 000 003 pwinslow@terrapetro-example.com.au
Office 02 5550 0100

Bulk Fuel deliveries.
Oils & lubricants
Local Family owned business

```html
<!DOCTYPE html>
<html lang="en">
<head>
<meta charset="utf-8">
<title>Terra Petro – Bulk Diesel Deliveries</title>
<link rel="stylesheet" href="https://fonts.googleapis.com/css2?family=Exo+2:ital,wght@1,900&family=Roboto+Condensed:wght@700&family=Russo+One&family=Poppins:wght@500;600;700&family=Michroma&display=swap">
<style>
  :root{
    --red:#e3201b;
    --red-dark:#b8120f;
    --black:#161616;
    --grey:#5e5e5e;
    --grey-panel:#6b6b6b;
    --sky-top:#6ccbee;
    --sky-bottom:#f3f8fb;
    --white:#ffffff;
    --line:#bdbdbd;
  }
  *{margin:0;padding:0;box-sizing:border-box}
  html,body{width:965px;height:1200px;overflow:hidden;background:#7b7a7a}
  .flyer{
    position:relative;width:965px;height:1200px;overflow:hidden;
    background:linear-gradient(180deg,var(--sky-top) 0%,#bfe5f4 25%,var(--sky-bottom) 50%,#f5f7f8 60%);
    font-family:"Poppins",sans-serif;color:var(--black);
  }
  .photo{
    position:absolute;left:0;top:640px;width:965px;height:420px;
    background:
      linear-gradient(160deg,transparent 55%,rgba(40,40,140,.85) 56%,#22239a 100%),
      linear-gradient(180deg,#b7bcc2 0%,#8f959c 45%,#e9ecee 60%,#c7cacd 78%,#3a3a3a 100%);
  }
  .footer-band{
    position:absolute;left:0;top:980px;width:965px;height:220px;
    background:linear-gradient(180deg,rgba(22,22,22,0) 0%,rgba(22,22,22,.85) 30%,#0d0d0d 70%,#050505 100%);
  }
  .headline-top{
    position:absolute;left:0;width:965px;top:40px;text-align:center;
    font:italic 900 104px/1 "Exo 2",sans-serif;color:var(--black);letter-spacing:2px;padding-left:80px;
  }
  .headline-sub{
    position:absolute;left:0;width:965px;top:136px;text-align:center;
    font:700 44px/1 "Roboto Condensed",sans-serif;color:var(--grey);padding-left:14px;
  }
  .headline-main{
    position:absolute;left:0;width:965px;top:168px;text-align:center;
    font:italic 900 142px/1 "Exo 2",sans-serif;color:var(--red);letter-spacing:4px;
  }
  .service-pill{
    position:absolute;left:90px;top:318px;width:784px;height:64px;border-radius:16px;overflow:hidden;
    display:flex;font:42px/64px "Russo One",sans-serif;color:var(--white);
  }
  .service-pill .dark{background:var(--black);width:405px;text-align:center;border-radius:16px;position:relative;z-index:1;box-shadow:3px 0 0 var(--white)}
  .service-pill .bright{background:var(--red);flex:1;text-align:center;margin-left:-16px;padding-left:16px}
  .feature{position:absolute;font:500 25px/1.3 "Poppins",sans-serif;color:var(--black)}
  .feature-icon{position:absolute;width:66px;height:66px}
  .divider-v{position:absolute;left:248px;top:422px;width:1px;height:140px;background:var(--line)}
  .divider-h{position:absolute;left:90px;top:580px;width:333px;height:1px;background:var(--line)}
  .family{position:absolute;left:171px;top:600px;font:24px/1.35 "Russo One",sans-serif;letter-spacing:1px}
  .family .accent{color:var(--red)}
  .area-panel{position:absolute;left:560px;top:408px}
  .area-text{
    position:absolute;left:679px;top:430px;
    font:700 38px/1.25 "Roboto Condensed",sans-serif;color:var(--white);
  }
  .pin{position:absolute;left:439px;top:408px}
  .pin-label{
    position:absolute;left:469px;top:480px;width:150px;text-align:center;
    font:500 21px/1.05 "Poppins",sans-serif;color:var(--black);
  }
  .pin-label b{display:block;font-weight:700;font-size:25px}
  .brand{
    position:absolute;left:40px;top:1080px;width:245px;text-align:center;
    font:600 44px/1 "Poppins",sans-serif;color:var(--white);
  }
  .footer-divider{position:absolute;top:1040px;width:1px;height:105px;background:#777}
  .contacts{position:absolute;left:318px;top:1040px;width:276px}
  .contact{
    display:flex;height:27px;margin-bottom:7px;border:1px solid #888;border-radius:14px;overflow:hidden;
    font:15px/25px "Michroma",sans-serif;color:var(--white);
  }
  .contact .name{background:var(--white);color:var(--black);width:93px;text-align:center;border-radius:14px}
  .contact .phone{padding-left:13px;letter-spacing:.5px}
  .order{position:absolute;left:636px;top:1040px;color:var(--white)}
  .order h2{font:22px/0.95 "Russo One",sans-serif;letter-spacing:1px;font-weight:400}
  .order h2 span{color:var(--red);display:block}
  .order-line{display:flex;align-items:center;gap:7px;font:700 14px/1 "Poppins",sans-serif;margin-top:12px}
  .order-line:first-of-type{margin-top:16px}
</style>
</head>
<body>
<div class="flyer">
  <div class="photo" role="img" aria-label="Photo of a fuel tanker road train parked beside a steel warehouse, with a waving Australian flag behind it"></div>
  <div class="footer-band"></div>

  <h1 class="headline-top">FUELING</h1>
  <p class="headline-sub">WHAT KEEPS OUR REGION</p>
  <p class="headline-main">MOVING</p>

  <div class="service-pill"><span class="dark">BULK DIESEL</span><span class="bright">DELIVERIES</span></div>

  <svg class="feature-icon" style="left:90px;top:427px" viewBox="0 0 66 66" aria-hidden="true">
    <circle cx="33" cy="33" r="31" fill="#fff" stroke="#5e5e5e" stroke-width="4"/>
    <circle cx="33" cy="33" r="25" fill="var(--red)"/>
    <rect x="23" y="26" width="20" height="18" rx="2" fill="none" stroke="#fff" stroke-width="2"/>
    <path d="M27 26v-4h8v4M43 30l5-4" stroke="#fff" stroke-width="2" fill="none"/>
    <path d="M20 18c-2 3-3 4-3 6a3 3 0 0 0 6 0c0-2-1-3-3-6z" fill="#fff"/>
    <circle cx="33" cy="36" r="3" fill="none" stroke="#fff" stroke-width="1.6"/>
  </svg>
  <p class="feature" style="left:90px;top:500px">Oils &amp;<br>lubricants</p>

  <div class="divider-v"></div>

  <svg class="feature-icon" style="left:275px;top:427px" viewBox="0 0 66 66" aria-hidden="true">
    <circle cx="33" cy="33" r="31" fill="#fff" stroke="#5e5e5e" stroke-width="4"/>
    <circle cx="33" cy="33" r="25" fill="var(--red)"/>
    <rect x="18" y="25" width="22" height="13" rx="2" fill="none" stroke="#fff" stroke-width="2"/>
    <path d="M40 29h6l4 5v4H40z" fill="none" stroke="#fff" stroke-width="2"/>
    <circle cx="24" cy="41" r="3" fill="#fff"/><circle cx="44" cy="41" r="3" fill="#fff"/>
  </svg>
  <p class="feature" style="left:275px;top:500px">Petrol<br>deliveries</p>

  <div class="divider-h"></div>

  <svg class="feature-icon" style="left:90px;top:614px" viewBox="0 0 66 66" aria-hidden="true">
    <circle cx="33" cy="33" r="31" fill="#fff" stroke="#5e5e5e" stroke-width="4"/>
    <circle cx="33" cy="33" r="25" fill="var(--red)"/>
    <circle cx="27" cy="24" r="3" fill="#fff"/><circle cx="39" cy="24" r="3" fill="#fff"/><circle cx="33" cy="29" r="2.5" fill="#fff"/>
    <path d="M19 32l6 10h16l6-10" fill="none" stroke="#fff" stroke-width="2.2" stroke-linejoin="round"/>
  </svg>
  <p class="family">LOCAL FAMILY<br><span class="accent">OWNED<br>BUSINESS</span></p>

  <svg class="area-panel" width="313" height="280" viewBox="0 0 313 280" aria-hidden="true">
    <path d="M20 0H293a20 20 0 0 1 20 20V150L60 280H0V20A20 20 0 0 1 20 0z" fill="var(--grey-panel)"/>
  </svg>
  <p class="area-text">Servicing<br>Griffith &amp;<br>surrounds</p>

  <svg class="pin" width="210" height="280" viewBox="0 0 210 280" aria-hidden="true">
    <path d="M105 278L22 168A104 104 0 1 1 188 168z" fill="var(--red)"/>
    <path d="M105 278L150 206" stroke="var(--red-dark)" stroke-width="3" opacity=".5"/>
    <circle cx="105" cy="104" r="80" fill="var(--red-dark)"/>
    <circle cx="105" cy="104" r="74" fill="#fff"/>
    <circle cx="105" cy="104" r="70" fill="none" stroke="#e6e6e6" stroke-width="2"/>
  </svg>
  <p class="pin-label">Based in<b>Griffith<br>NSW</b></p>

  <p class="brand">Terra Petro</p>
  <div class="footer-divider" style="left:300px"></div>

  <div class="contacts">
    <div class="contact"><span class="name">Marco</span><span class="phone">0400 000 001</span></div>
    <div class="contact"><span class="name">Liam</span><span class="phone">0400 000 002</span></div>
    <div class="contact"><span class="name">Peter</span><span class="phone">0400 000 003</span></div>
  </div>

  <div class="footer-divider" style="left:612px"></div>

  <div class="order">
    <h2>PLACE YOUR<span>ORDER</span></h2>
    <p class="order-line">
      <svg width="16" height="16" viewBox="0 0 16 16" aria-hidden="true"><circle cx="8" cy="8" r="8" fill="var(--red)"/><rect x="4" y="5" width="8" height="6" fill="none" stroke="#fff" stroke-width="1.2"/><path d="M4 5l4 3 4-3" fill="none" stroke="#fff" stroke-width="1.2"/></svg>
      Fuel@terrapetro-example.com.au
    </p>
    <p class="order-line">
      <svg width="16" height="16" viewBox="0 0 16 16" aria-hidden="true"><circle cx="8" cy="8" r="8" fill="var(--red)"/><circle cx="8" cy="8" r="4.5" fill="none" stroke="#fff" stroke-width="1.2"/><path d="M3.5 8h9M8 3.5v9" stroke="#fff" stroke-width="1"/></svg>
      www.terrapetro-example.com.au
    </p>
  </div>
</div>
</body>
</html>
```